CBD PATCHES

Design creation of my CBD patch box.
Product must look Pharamaceutical grade.
Colours need to look pharmaceutical (green/white/maybe a bit of blue).
Text: Cannabidiol (CBD) Self-curing adhesive Polyethylene backing sheet.
Apply one patch to a smooth are of skin. Each patch can be worn for up to 24 hours. Apply subsequent patches to different areas to allow the skin to breathe between uses.
Do not apply to broken or irritable skin. Consult a doctor if you are taking medications or have medical conditions before using this or any other supplement. Do not use if you are pregnant or breastfeeding.
Store in a cool, dry place out of direct sunlight. Stable for three years. Once opened, use within 12 months.

```html
<!DOCTYPE html>
<html lang="en">
<head>
<meta charset="utf-8">
<title>Dermaleaf CBD Patches – Box Dieline</title>
<link rel="stylesheet" href="https://fonts.googleapis.com/css2?family=Cutive+Mono&display=swap">
<style>
  :root {
    --paper: #ffffff;
    --leaf-green: #abd087;
    --leaf-green-faint: #bedba0;
    --warning-grey: #c8c8c8;
    --cut-line: #333333;
    --ink: #2e2e2e;
  }
  html, body {
    margin: 0;
    padding: 0;
    width: 1200px;
    height: 908px;
    overflow: hidden;
    background: var(--paper);
  }
  .dieline {
    display: block;
    width: 1200px;
    height: 908px;
  }
  .cut { fill: none; stroke: var(--cut-line); stroke-width: 1.6; }
  .paper { fill: var(--paper); stroke: var(--cut-line); stroke-width: 1.6; }
  .panel-green { fill: var(--leaf-green); stroke: var(--cut-line); stroke-width: 1.6; }
  .tab-green { fill: var(--leaf-green); }
  .warning-box { fill: var(--warning-grey); }
  .copy {
    font-family: "Cutive Mono", "Courier New", monospace;
    fill: var(--ink);
    font-size: 21.5px;
  }
  .product-name { font-size: 31px; }
  .product-spec { font-size: 19px; letter-spacing: 0.5px; }
  .brand-name {
    font-family: "Cutive Mono", "Courier New", monospace;
    fill: var(--leaf-green);
    font-size: 44px;
    letter-spacing: 2px;
  }
  .brand-tagline {
    font-family: "Cutive Mono", "Courier New", monospace;
    fill: var(--leaf-green);
    font-size: 22px;
    letter-spacing: 2px;
  }
  .brand-mark { fill: var(--leaf-green); }
  .brand-mark-faint { fill: var(--leaf-green-faint); }
  .brand-name-faint {
    font-family: "Cutive Mono", "Courier New", monospace;
    fill: var(--leaf-green-faint);
    font-size: 40px;
    letter-spacing: 2px;
  }
</style>
</head>
<body>
<svg class="dieline" viewBox="0 0 2200 1665" xmlns="http://www.w3.org/2000/svg" aria-label="Dermaleaf CBD patch box dieline, outer and inner sides">

  <!-- ========== Outer side ========== -->
  <g class="box-outer">
    <!-- top tuck flap -->
    <path class="paper" d="M316,340 C350,336 360,300 362,270 L362,89 L509,89 A79,80 0 0 0 667,89 L806,89 L806,270 C808,300 818,336 852,340 Z"/>
    <!-- side dust flaps -->
    <path class="paper" d="M316,342 L128,342 L128,605 C130,730 200,830 316,835 Z"/>
    <path class="paper" d="M852,339 L1048,339 L1048,605 C1025,730 950,830 852,832 Z"/>
    <line class="cut" x1="187" y1="573" x2="280" y2="482"/>
    <line class="cut" x1="906" y1="479" x2="995" y2="570"/>

    <!-- bottom tab -->
    <path class="tab-green" d="M484,1510 C490,1560 530,1588 582,1588 C634,1588 674,1560 679,1510 Z"/>
    <path class="cut" d="M484,1513 C490,1560 530,1588 582,1588 C634,1588 674,1560 679,1513"/>

    <!-- top panel: storage -->
    <rect class="panel-green" x="316" y="340" width="536" height="465"/>
    <polyline class="cut" points="473,423 487,403 679,403 691,423"/>
    <g class="copy storage-copy" transform="rotate(180 585 605)">
      <text x="356" y="570" textLength="457" lengthAdjust="spacing">Store in a cool, dry place out of</text>
      <text x="356" y="599" textLength="457" lengthAdjust="spacing">direct sunlight. Stable for three</text>
      <text x="356" y="627" textLength="457" lengthAdjust="spacing">years. Once opened, use within 12</text>
      <text x="356" y="655">months.</text>
    </g>

    <!-- front panel -->
    <rect class="paper" x="316" y="805" width="536" height="482"/>
    <circle class="brand-mark" cx="578" cy="938" r="116"/>
    <text class="brand-name" x="578" y="1112" text-anchor="middle">DERMALEAF</text>
    <text class="brand-tagline" x="578" y="1143" text-anchor="middle">CBD PATCHES</text>
    <text class="copy product-name" x="580" y="1197" text-anchor="middle">Cannabidiol (CBD)</text>
    <text class="copy product-spec" x="580" y="1229" text-anchor="middle">Self-curing adhesive</text>
    <text class="copy product-spec" x="580" y="1261" text-anchor="middle">Polyethylene backing sheet</text>

    <!-- bottom panel -->
    <rect class="panel-green" x="316" y="1287" width="536" height="226"/>
    <line x1="486" y1="1513" x2="677" y2="1513" stroke="var(--leaf-green)" stroke-width="3"/>
  </g>

  <!-- ========== Inner side ========== -->
  <g class="box-inner">
    <!-- top tab -->
    <path class="tab-green" d="M1515,168 C1520,120 1560,89 1612,89 C1664,89 1706,120 1710,168 Z"/>
    <path class="cut" d="M1515,165 C1520,120 1560,89 1612,89 C1664,89 1704,118 1708,165"/>

    <!-- top panel -->
    <rect class="panel-green" x="1341" y="165" width="536" height="226"/>
    <line x1="1530" y1="165" x2="1692" y2="165" stroke="var(--leaf-green)" stroke-width="3"/>

    <!-- directions panel -->
    <rect class="paper" x="1341" y="391" width="536" height="481"/>
    <g class="copy directions-copy">
      <text x="1369" y="462" textLength="481" lengthAdjust="spacing">Apply one patch to a smooth are of skin.</text>
      <text x="1369" y="490" textLength="481" lengthAdjust="spacing">Each patch can be worn for up to 24</text>
      <text x="1369" y="518" textLength="481" lengthAdjust="spacing">hours. Apply subsequent patches to dif-</text>
      <text x="1369" y="547" textLength="481" lengthAdjust="spacing">ferent areas to allow the skin to</text>
      <text x="1369" y="575">breathe between uses.</text>
    </g>
    <rect class="warning-box" x="1351" y="632" width="513" height="209"/>
    <g class="copy warning-copy">
      <text x="1369" y="676" textLength="481" lengthAdjust="spacing">Do not apply to broken or irritable</text>
      <text x="1369" y="704" textLength="481" lengthAdjust="spacing">skin. Consult a doctor if you are taking</text>
      <text x="1369" y="732" textLength="481" lengthAdjust="spacing">medications or have medical conditions</text>
      <text x="1369" y="761" textLength="481" lengthAdjust="spacing">before using this or any other supple-</text>
      <text x="1369" y="789" textLength="481" lengthAdjust="spacing">ment. Do not use if you are pregnant or</text>
      <text x="1369" y="817">breastfeeding.</text>
    </g>

    <!-- side dust flaps -->
    <path class="paper" d="M1341,845 C1230,850 1160,950 1143,1070 L1143,1339 L1341,1339 Z"/>
    <path class="paper" d="M1877,842 C1990,848 2060,950 2065,1070 L2065,1336 L1877,1336 Z"/>
    <line class="cut" x1="1197" y1="1108" x2="1287" y2="1199"/>
    <line class="cut" x1="2006" y1="1106" x2="1912" y2="1197"/>

    <!-- back panel -->
    <rect class="panel-green" x="1341" y="872" width="536" height="465"/>
    <circle class="brand-mark-faint" cx="1610" cy="1050" r="90"/>
    <text class="brand-name-faint" x="1610" y="1190" text-anchor="middle">DERMALEAF</text>
    <polyline class="cut" points="1502,1255 1515,1275 1705,1275 1719,1255"/>

    <!-- bottom tuck flap -->
    <path class="paper" d="M1341,1339 C1375,1343 1385,1380 1387,1410 L1387,1588 L1526,1588 A79,80 0 0 1 1684,1588 L1831,1588 L1831,1410 C1833,1380 1843,1343 1877,1339 Z"/>
  </g>
</svg>
</body>
</html>
```